Website Required for Small Cyber Security Company

Require a website for Cyber Security company. I have logo which i will attach. Please use logo blue and white as a guide
Would ultimately like the site to have a technology theme with the following pages Landing page
Services
Contact
Careers

I can provide content for each of those pages in due course, until then happy for you to use dummy data to display purposes

Target Market(s)

Government

Industry/Entity Type

Cyber Security

Coding

Coded - Design and coding required

Number of Pages Required

4 page

Colors
0054AA
0677BA
7BADD7
CADEEF
E8F1F8

Requirements
Must have
• High quality finish and UX
Nice to have
• look and feel professional and not cheap

```html
<!DOCTYPE html>
<html lang="en">
<head>
<meta charset="utf-8">
<title>Harlow Ridge Consulting — Cyber Security</title>
<link href="https://fonts.googleapis.com/css2?family=Plus+Jakarta+Sans:wght@500;600;700;800&family=Inter:wght@400;500;600&display=swap" rel="stylesheet">
<style>
:root{
  --navy:#0b2a55;
  --deep:#0a2347;
  --blue:#0054AA;
  --mid:#0677BA;
  --light:#7BADD7;
  --pale:#CADEEF;
  --mist:#E8F1F8;
  --white:#ffffff;
  --ink:#1d2f4f;
  --muted:#4e5d78;
  --footer:#262626;
  --card-grad:linear-gradient(180deg,#0a76b0 0%,#6e9fc6 100%);
  --head:"Plus Jakarta Sans",sans-serif;
  --body:"Inter",sans-serif;
}
*{box-sizing:border-box;margin:0;padding:0}
html,body{width:1200px;height:4675px;overflow:hidden}
body{font-family:var(--body);color:var(--ink);background:var(--white);position:relative}
section,header,footer{position:absolute;left:0;width:1200px}
.abs{position:absolute}
h1,h2,h3{font-family:var(--head);letter-spacing:-0.5px}
.btn-pill{display:inline-flex;align-items:center;justify-content:center;border-radius:30px;background:linear-gradient(180deg,#0a76b0,#5d97c6);color:var(--white);font-size:14px;font-weight:500}
.btn-outline{display:inline-flex;align-items:center;justify-content:center;border:1.5px solid var(--white);border-radius:3px;color:var(--white);font-size:11px;width:110px;height:34px}
.btn-solid{display:inline-flex;align-items:center;justify-content:center;background:var(--white);color:var(--mid);border-radius:3px;font-size:11px;width:110px;height:34px}

/* header */
.site-header{top:0;height:95px;background:var(--white)}
.brand{left:72px;top:14px;display:flex;flex-direction:column;align-items:center;gap:4px}
.brand-mark{width:34px;height:34px;border-radius:50%;background:var(--mid)}
.brand-name{font-family:var(--head);font-weight:700;font-size:12px;color:var(--navy);line-height:1.1;text-align:center}
.nav{left:403px;top:38px;display:flex;gap:30px;font-size:13px;font-weight:500;color:var(--ink)}
.nav .active{color:var(--mid)}
.get-started{left:995px;top:28px;width:137px;height:38px;font-size:12px;font-weight:600}

/* hero */
.hero{top:95px;height:615px;background:linear-gradient(90deg,#0d2a55 0%,#26456f 55%,#3a5c85 100%)}
.hero-photo{inset:0;background:linear-gradient(100deg,rgba(12,40,82,.85) 0%,rgba(40,70,110,.55) 60%,rgba(90,110,135,.45) 100%)}
.hero h1{left:73px;top:110px;width:520px;font-size:51px;font-weight:800;line-height:1.15;color:var(--white)}
.hero p{left:73px;top:305px;width:560px;font-size:13.5px;line-height:1.55;color:var(--white)}
.hero .btn-pill{left:73px;top:362px;width:172px;height:48px}

/* feature cards */
.feature{top:641px;width:290px;height:404px;background:var(--card-grad);color:var(--white);text-align:center;padding:40px 26px 0}
.feature.lift{top:615px;width:274px;height:458px;padding-top:52px}
.feature svg{width:62px;height:62px;margin-bottom:18px}
.feature h3{font-size:26px;font-weight:700;line-height:1.5;margin-bottom:16px}
.feature p{font-size:13px;line-height:1.55;margin-bottom:26px}

/* about */
.about{top:1160px;height:640px}
.about-photo{left:69px;top:15px;width:523px;height:589px;background:linear-gradient(160deg,#c9b9a3 0%,#8d8778 45%,#5a6678 100%)}
.badge{left:401px;top:7px;width:200px;height:160px;background:var(--card-grad);color:var(--white);text-align:center;padding-top:40px}
.badge strong{display:block;font-family:var(--head);font-size:48px;font-weight:800;line-height:1}
.badge span{font-size:13px;font-weight:600}
.about h2{left:695px;top:172px;width:440px;font-size:36px;font-weight:700;line-height:1.35;color:var(--navy)}
.about p{left:695px;top:287px;width:420px;font-size:13px;line-height:1.6;color:var(--muted)}
.about .btn-pill{left:695px;top:399px;width:172px;height:48px}

/* services grid */
.services{top:1870px;height:869px;background:linear-gradient(180deg,#0b2a55 0%,#0a2448 100%)}
.services-bg{right:0;top:0;width:520px;height:420px;background:radial-gradient(ellipse at 80% 20%,rgba(60,110,170,.35),transparent 70%)}
.services h2{left:0;width:1200px;top:92px;text-align:center;font-size:36px;font-weight:700;line-height:1.4;color:var(--white)}
.services .lead{left:0;width:1200px;top:208px;text-align:center;font-size:13px;color:var(--pale)}
.svc{width:343px;height:236px;background:var(--card-grad);color:var(--white);text-align:center;padding-top:90px}
.svc h3{font-family:var(--body);font-size:15px;font-weight:600;letter-spacing:0;margin-bottom:14px}
.svc p{font-size:13px;line-height:1.55;padding:0 50px;margin-bottom:12px}
.svc .tag{display:inline-block;background:var(--blue);color:var(--white);font-size:10px;padding:6px 16px;border-radius:2px}

/* stats */
.stats{top:2739px;height:584px;background:var(--white)}
.world{left:80px;top:20px;width:1040px;height:560px;background:radial-gradient(ellipse at center,rgba(202,222,239,.35),transparent 70%)}
.stats h2{left:0;width:1200px;top:110px;text-align:center;font-size:36px;font-weight:700;line-height:1.4;color:var(--navy)}
.stats p{left:270px;width:660px;top:226px;text-align:center;font-size:13px;line-height:1.6;color:var(--muted)}
.stat{top:307px;width:220px;height:126px;background:var(--card-grad);color:var(--white);text-align:center;padding-top:26px}
.stat strong{display:block;font-family:var(--head);font-size:38px;font-weight:700;line-height:1.2}
.stat span{font-size:14px;font-weight:600}

/* privacy band */
.privacy{top:3323px;height:465px;background:linear-gradient(90deg,#123a6e 0%,#1d4d82 45%,#173e66 100%)}
.privacy-photo{inset:0;background:linear-gradient(90deg,rgba(18,58,110,.2) 0%,rgba(30,70,110,.4) 60%,rgba(20,45,75,.7) 100%)}
.privacy h2{left:88px;top:118px;width:520px;font-size:36px;font-weight:700;line-height:1.4;color:var(--white)}
.privacy p{left:88px;top:240px;width:490px;font-size:13px;line-height:1.55;color:var(--pale)}
.privacy .btn-sq{left:88px;top:307px;width:142px;height:37px;background:var(--mid);color:var(--light);font-size:13px;display:flex;align-items:center;justify-content:center}

/* testimonials */
.testimonials{top:3788px;height:546px;background:var(--white)}
.testimonials h2{left:0;width:1200px;top:76px;text-align:center;font-size:36px;font-weight:700;color:var(--navy)}
.testimonials .lead{left:340px;width:520px;top:152px;text-align:center;font-size:13px;line-height:1.6;color:var(--muted)}
.quote{top:216px;width:347px;height:229px;background:#0a76a8;color:var(--white);text-align:center;padding:32px 26px 0}
.quote p{font-size:14px;line-height:1.5;margin-bottom:22px}
.author{display:flex;align-items:center;justify-content:center;gap:14px;font-size:11px}
.avatar{width:40px;height:40px;border-radius:50%;background:linear-gradient(180deg,#e8e3dc,#b7aca0);border:2px solid var(--white)}
.dots{left:0;width:1200px;top:460px;display:flex;justify-content:center;gap:14px}
.dots i{width:10px;height:10px;border-radius:50%;background:var(--navy)}

/* footer */
.site-footer{top:4334px;height:276px;background:var(--footer);color:var(--white)}
.site-footer h4{font-family:var(--head);font-weight:700}
.news h4{position:absolute;left:73px;top:64px;font-size:24px}
.news p{position:absolute;left:73px;top:112px;width:340px;font-size:15px;line-height:1.55}
.email{position:absolute;left:73px;top:180px;width:216px;height:38px;border:2px solid var(--mid);background:#1f4e7a;font-size:13px;color:var(--pale);padding:9px 14px}
.signup{position:absolute;left:296px;top:180px;width:142px;height:38px;background:var(--blue);color:#1a4f86;font-size:13px;display:flex;align-items:center;justify-content:center}
.fcol{position:absolute;top:62px}
.fcol h4{font-size:14px;margin-bottom:20px}
.fcol li{list-style:none;font-size:11.5px;line-height:24.5px;padding-left:18px}
.social{display:flex;gap:8px}
.social span{width:40px;height:40px;border-radius:50%;background:var(--white)}
.copyright{position:absolute;left:0;top:276px;width:1200px;height:65px;background:var(--mid);color:var(--white);font-size:11px;text-align:center;line-height:65px}
</style>
</head>
<body>

<header class="site-header">
  <div class="abs brand">
    <span class="brand-mark"></span>
    <span class="brand-name">HARLOW RIDGE<br>CONSULTING</span>
  </div>
  <nav class="abs nav">
    <span class="active">HOME</span><span>ABOUT</span><span>SERVICES</span><span>CAREERS</span><span>CONTACT</span>
  </nav>
  <a class="abs btn-pill get-started">GET STARTED</a>
</header>

<section class="hero">
  <div class="abs hero-photo" role="img" aria-label="Family using a laptop together on a sofa at home"></div>
  <h1 class="abs">Secure your cyberspace, secure your digital life.</h1>
  <p class="abs">Natoque elit torquent a primis si feugiat fames felis phasellus vulputate molestie. Pharetra praesent amet vulputate laoreet scelerisque.</p>
  <a class="abs btn-pill">Discover more</a>
</section>

<div class="abs feature" style="left:158px">
  <svg viewBox="0 0 64 64" fill="none" stroke="#fff" stroke-width="2.5"><circle cx="32" cy="32" r="28"/><ellipse cx="32" cy="32" rx="12" ry="28"/><line x1="4" y1="32" x2="60" y2="32"/><path d="M8 18h48M8 46h48"/></svg>
  <h3>Protect your privacy</h3>
  <p>Lorem ipsum dolor sit amet, consectetur adipiscing elit. Ut elit tellus, luctus nec ullamcorper mattis, pulvinar dapibus leo.</p>
  <span class="btn-outline">Learn more</span>
</div>
<div class="abs feature lift" style="left:463px">
  <svg viewBox="0 0 64 64" fill="none" stroke="#fff" stroke-width="3" stroke-linecap="round"><path d="M4 24a40 40 0 0 1 56 0"/><path d="M13 33a27 27 0 0 1 38 0"/><path d="M22 42a14 14 0 0 1 20 0"/><circle cx="32" cy="52" r="3.5"/></svg>
  <h3>Real-time protection</h3>
  <p>Lorem ipsum dolor sit amet, consectetur adipiscing elit. Ut elit tellus, luctus nec ullamcorper mattis, pulvinar dapibus leo.</p>
  <span class="btn-solid">Learn more</span>
</div>
<div class="abs feature" style="left:751px">
  <svg viewBox="0 0 64 64" fill="none" stroke="#fff" stroke-width="2.5"><circle cx="32" cy="30" r="26"/><circle cx="20" cy="36" r="5"/><circle cx="32" cy="33" r="5"/><circle cx="44" cy="36" r="5"/><path d="M12 56c0-8 16-8 16 0M24 54c0-8 16-8 16 0M36 56c0-8 16-8 16 0"/></svg>
  <h3>Secure your identity</h3>
  <p>Lorem ipsum dolor sit amet, consectetur adipiscing elit. Ut elit tellus, luctus nec ullamcorper mattis, pulvinar dapibus leo.</p>
  <span class="btn-outline">Learn more</span>
</div>

<section class="about">
  <div class="abs about-photo" role="img" aria-label="Smiling senior man working on a laptop"></div>
  <div class="abs badge"><strong>20+</strong><span>Years Experience</span></div>
  <h2 class="abs">Maximum protection for all your devices.</h2>
  <p class="abs">Lorem ipsum dolor sit amet, consectetur adipiscing elit. Ut elit tellus, luctus nec ullamcorper mattis, pulvinar dapibus leo. Lorem ipsum dolor sit amet, consectetur adipiscing elit. Ut elit tellus, luctus nec ullamcorper mattis, pulvinar dapibus leo.</p>
  <a class="abs btn-pill">Discover more</a>
</section>

<section class="services">
  <div class="abs services-bg" role="img" aria-label="Faint glowing lines of code"></div>
  <h2 class="abs">Secure Your Data, Secure Your<br>Future.</h2>
  <p class="abs lead">Lorem ipsum dolor sit amet, consectetur adipiscing elit.</p>
  <div class="abs svc" style="left:69px;top:275px"><h3>Network Protections</h3><p>Ipsum duis nisl eget ut sed phasellus molestie vivamus euismod.</p><span class="tag">Learn more</span></div>
  <div class="abs svc" style="left:428px;top:275px"><h3>Server Protections</h3><p>Ipsum duis nisl eget ut sed phasellus molestie vivamus euismod.</p><span class="tag">Learn more</span></div>
  <div class="abs svc" style="left:788px;top:275px"><h3>Vulnerability Assessment</h3><p>Ipsum duis nisl eget ut sed phasellus molestie vivamus euismod.</p><span class="tag">Learn more</span></div>
  <div class="abs svc" style="left:69px;top:530px"><h3>SPAM Protections</h3><p>Ipsum duis nisl eget ut sed phasellus molestie vivamus euismod.</p><span class="tag">Learn more</span></div>
  <div class="abs svc" style="left:428px;top:530px"><h3>Secure Transactions</h3><p>Ipsum duis nisl eget ut sed phasellus molestie vivamus euismod.</p><span class="tag">Learn more</span></div>
  <div class="abs svc" style="left:788px;top:530px"><h3>Antivirus</h3><p>Ipsum duis nisl eget ut sed phasellus molestie vivamus euismod.</p><span class="tag">Learn more</span></div>
</section>

<section class="stats">
  <div class="abs world" role="img" aria-label="Faint dotted world map"></div>
  <h2 class="abs">Security monitoring and malware<br>protection for businesses.</h2>
  <p class="abs">Lorem ipsum dolor sit amet, consectetur adipiscing elit. Ut elit tellus, luctus nec ullamcorper mattis, pulvinar dapibus leo.</p>
  <div class="abs stat" style="left:254px"><strong>14K+</strong><span>Happy Customer</span></div>
  <div class="abs stat" style="left:490px"><strong>98%</strong><span>Uptime Server</span></div>
  <div class="abs stat" style="left:726px"><strong>12K+</strong><span>Project Done</span></div>
</section>

<section class="privacy">
  <div class="abs privacy-photo" role="img" aria-label="Analyst working at a desk with several monitors"></div>
  <h2 class="abs">Data privacy is a human right and it belongs to you</h2>
  <p class="abs">Lorem ipsum dolor sit amet, consectetur adipiscing elit. Ut elit tellus, luctus nec ullamcorper mattis, pulvinar dapibus leo.</p>
  <a class="abs btn-sq">Discover more</a>
</section>

<section class="testimonials">
  <h2 class="abs">What they say about us.</h2>
  <p class="abs lead">Lorem ipsum dolor sit amet, consectetur adipiscing elit. Ut elit tellus, luctus nec ullamcorper mattis, pulvinar dapibus leo.</p>
  <div class="abs quote" style="left:60px"><p>Lorem ipsum dolor sit amet, consectetur adipiscing elit. Ut elit tellus, luctus nec ullamcorper mattis, pulvinar dapibus leo.</p><div class="author"><span class="avatar" role="img" aria-label="Client portrait"></span>CEO Velto</div></div>
  <div class="abs quote" style="left:427px"><p>Lorem ipsum dolor sit amet, consectetur adipiscing elit. Ut elit tellus, luctus nec ullamcorper mattis, pulvinar dapibus leo.</p><div class="author"><span class="avatar" role="img" aria-label="Client portrait"></span>Business Manager</div></div>
  <div class="abs quote" style="left:791px"><p>Lorem ipsum dolor sit amet, consectetur adipiscing elit. Ut elit tellus, luctus nec ullamcorper mattis, pulvinar dapibus leo.</p><div class="author"><span class="avatar" role="img" aria-label="Client portrait"></span>Founder Brisk</div></div>
  <div class="abs dots"><i></i><i></i><i></i></div>
</section>

<footer class="site-footer">
  <div class="news">
    <h4>Newsletter</h4>
    <p>Signup our newsletter to get update information, news, insight or promotions.</p>
    <div class="email">Email</div>
    <div class="signup">Sign Up ✉</div>
  </div>
  <div class="fcol" style="left:506px">
    <h4>Services</h4>
    <ul><li>Network Protections</li><li>Server Protections</li><li>Secure IT Infrastructure</li><li>Vulnerability Assessment</li><li>Secure Transactions</li><li>Antivirus</li></ul>
  </div>
  <div class="fcol" style="left:722px">
    <h4>Support</h4>
    <ul><li>Help Center</li><li>Ticket Support</li><li>FAQ</li><li>Contact us</li><li>Community</li></ul>
  </div>
  <div class="fcol" style="left:938px">
    <h4>Follow Us</h4>
    <div class="social"><span></span><span></span><span></span></div>
  </div>
  <div class="copyright">Copyright © 2022 harlowridge, All rights reserved. Powered by Fernline Studio.</div>
</footer>

</body>
</html>
```